Quorvane Limited needs a business card design

We need a business card design that reflects both professionalism and innovation and captures our brand identity. We provide online enterprise solutions to HR and executive management. We would like to use the colors in our logo (Blue and Orange). See attached file.

We would like a more creative design than the existing attached business card but maintain the same information on it.

To see our products site, please visit www.quorvane.example which reflects more our identity
Updates

Please see our site: www.quorvane.example, not www.quorvane.example.uk for our colors and look and feel

Target Market(s)

Senior Executives

Industry/Entity Type

Business

Requirements
Must have
• Logo and use of logo colors
Nice to have
• Icons
Should not have
• Images

```html
<!DOCTYPE html>
<html lang="en">
<head>
<meta charset="utf-8">
<title>Quorvane Limited – Business Card</title>
<link rel="stylesheet" href="https://fonts.googleapis.com/css2?family=Lato:wght@400;700;900&display=swap">
<style>
  :root {
    --brand-blue: #1565b3;
    --brand-orange: #ee6f1c;
    --ink: #1d1d1d;
    --paper: #ffffff;
    --paper-top: #f1f1f1;
    --backdrop: #d9dbde;
  }
  * { box-sizing: border-box; margin: 0; padding: 0; }
  html, body {
    width: 1200px; height: 926px; overflow: hidden;
    background: var(--backdrop);
    font-family: 'Lato', sans-serif;
    color: var(--ink);
  }
  .card {
    position: absolute;
    left: 240px;
    width: 720px; height: 410px;
    background: var(--paper);
    overflow: hidden;
    box-shadow: 0 6px 18px rgba(0,0,0,.18);
  }
  .card--front { top: 30px; }
  .card--back { top: 486px; background: linear-gradient(#fafafa, var(--paper-top)); }

  /* Front */
  .wordmark {
    position: absolute; left: 40px; top: 32px;
    font-size: 66px; font-weight: 900; color: var(--brand-blue);
    letter-spacing: -1px;
  }
  .holder { position: absolute; right: 44px; top: 140px; text-align: right; }
  .holder__name { font-size: 36px; font-weight: 400; line-height: 1.1; }
  .holder__name strong { font-weight: 900; }
  .holder__title { font-size: 21px; font-weight: 700; color: var(--brand-orange); }

  .contact__badge {
    position: absolute; left: 0; display: flex; align-items: center; justify-content: center;
  }
  .contact__badge--phone { top: 168px; width: 44px; height: 44px; background: var(--brand-orange); }
  .contact__badge--mail { top: 236px; width: 44px; height: 28px; background: var(--brand-blue); }
  .contact__phones {
    position: absolute; left: 60px; top: 164px;
    list-style: none; font-size: 19px; line-height: 23px;
  }
  .contact__email { position: absolute; left: 60px; top: 238px; font-size: 19px; }

  .company { position: absolute; right: 44px; top: 234px; text-align: right; }
  .company__name { font-size: 28px; font-weight: 900; color: var(--brand-blue); }
  .company__address { font-size: 20px; line-height: 24px; letter-spacing: .5px; }

  .swoosh { position: absolute; left: 0; top: 0; width: 720px; height: 410px; }
  .web {
    position: absolute; right: 44px; bottom: 10px;
    font-size: 20px; font-weight: 700; color: var(--paper); letter-spacing: 2px;
  }

  /* Back */
  .back__head { position: absolute; top: 34px; width: 100%; text-align: center; }
  .back__company { font-size: 30px; font-weight: 900; letter-spacing: 1px; }
  .back__tagline { font-size: 15px; letter-spacing: .5px; text-transform: uppercase; }
  .back__wordmark {
    position: absolute; top: 110px; width: 100%; text-align: center;
    font-size: 72px; font-weight: 900; color: var(--brand-blue); letter-spacing: -1px;
  }
  .back__registration {
    position: absolute; top: 212px; width: 100%; text-align: center;
    font-size: 15px; line-height: 19px; letter-spacing: .4px; text-transform: uppercase;
  }
  .back__band {
    position: absolute; left: 0; bottom: 0; width: 100%; height: 140px;
    background: var(--brand-blue); color: var(--paper); text-align: center;
    padding-top: 30px;
  }
  .back__office-label { font-size: 18px; font-weight: 900; letter-spacing: 1px; }
  .back__office { font-size: 16px; letter-spacing: .4px; margin-top: 4px; }
</style>
</head>
<body>

<section class="card card--front">
  <svg class="swoosh" viewBox="0 0 720 410" aria-hidden="true">
    <path d="M0 296 C160 292 320 304 500 326 C320 312 160 308 0 310 Z" fill="var(--brand-orange)"/>
    <path d="M0 322 C240 318 480 352 720 366 L720 410 L0 410 Z" fill="var(--brand-blue)"/>
  </svg>

  <div class="wordmark">Quorvane</div>

  <div class="holder">
    <div class="holder__name">Maren <strong>Talvik</strong></div>
    <div class="holder__title">Managing Director</div>
  </div>

  <div class="contact__badge contact__badge--phone">
    <svg width="22" height="22" viewBox="0 0 24 24" aria-hidden="true">
      <path d="M6.6 10.8a15 15 0 0 0 6.6 6.6l2.2-2.2c.3-.3.7-.4 1-.2 1.1.4 2.3.6 3.6.6.6 0 1 .4 1 1V20c0 .6-.4 1-1 1A17 17 0 0 1 3 4c0-.6.4-1 1-1h3.5c.6 0 1 .4 1 1 0 1.3.2 2.5.6 3.6.1.3 0 .7-.2 1z" fill="#fff"/>
    </svg>
  </div>
  <ul class="contact__phones">
    <li>+4420 5550 1184</li>
    <li>+132 555 09273</li>
    <li>+961 555 30618</li>
  </ul>

  <div class="contact__badge contact__badge--mail">
    <svg width="22" height="16" viewBox="0 0 22 16" aria-hidden="true">
      <rect x="1" y="1" width="20" height="14" fill="none" stroke="#fff" stroke-width="1.6"/>
      <path d="M1 1 L11 9 L21 1" fill="none" stroke="#fff" stroke-width="1.6"/>
    </svg>
  </div>
  <div class="contact__email">mtalvik@quorvane.example.uk</div>

  <div class="company">
    <div class="company__name">Quorvane Limited</div>
    <div class="company__address">1208 Harwell House,<br>54 Linden Row, London, N1 4QX</div>
  </div>

  <div class="web">www.quorvane.example.uk</div>
</section>

<section class="card card--back">
  <div class="back__head">
    <div class="back__company">QUORVANE LIMITED</div>
    <div class="back__tagline">Developing leaders and organisations</div>
  </div>
  <div class="back__wordmark">Quorvane</div>
  <div class="back__registration">
    Quorvane Limited is a company registered in England &amp; Wales<br>
    with company number 04518263
  </div>
  <div class="back__band">
    <div class="back__office-label">REGISTERED OFFICE</div>
    <div class="back__office">Mill House, Orchard Lane, Eastfold, Surrey, KT9 4ZX</div>
  </div>
</section>

</body>
</html>
```